Bluestone Advisory & Mgmt - Professional Business Cards

Hi!

I am a Real Estate Developer and Construction Consultant.

I have a lot of inspiration from previous designs and would be open to using the attached Designs as a starting point. I would like to see these styles incorporated into your designs.

I really need professional business card to go with it that includes my important info.

Look forward to seeing your designs!.

Target Market(s)

My Target market are building owners, lawyers, consultants.

Industry/Entity Type

Real Estate Development

Contact Information for Business Card

My Name: Dorian Pelkey
My Title: Principle
Company Name: Bluestone Advisory & Mgmt, LLC
Address: 348 West 71st Street, 9th FL New York, NY 10010
Mobile: 917.806.3971
Website: bam-hvx.example

Font styles to use
Serif
Sans Serif

Colors

Designer to choose colors to be used in the design.

Requirements
Must have
• Must incorporate the logo attached or have new that looks similar.
• Must use professional font that will be seen and judged by wealthy land owners and developers.
• Must incorporate some of the color green.
Should not have
• Photo's or pictures of people or buildings of any kind.

```html
<!DOCTYPE html>
<html lang="en">
<head>
<meta charset="utf-8">
<title>Bluestone Advisory &amp; Mgmt – Business Cards</title>
<link rel="stylesheet" href="https://fonts.googleapis.com/css2?family=Montserrat:wght@500;600&family=Lora:wght@400&family=Allura&display=swap">
<style>
  :root {
    --page: #e6e2dc;
    --card-black: #0a0a0a;
    --brand-green: #00a86b;
    --silver: #c9c9c9;
    --white: #f4f4f4;
  }
  * { box-sizing: border-box; margin: 0; padding: 0; }
  html, body {
    width: 1200px; height: 843px; overflow: hidden;
    background: var(--page);
  }
  .sheet {
    width: 1200px; height: 843px;
    display: flex; align-items: center; justify-content: center; gap: 40px;
  }
  .card {
    position: relative;
    width: 540px; height: 309px;
    background: var(--card-black);
    overflow: hidden;
    box-shadow: 0 6px 18px rgba(0,0,0,.18);
  }

  /* Front */
  .card-front {
    display: flex; align-items: center; justify-content: center;
  }
  .brand-large {
    display: flex; align-items: center; gap: 16px;
  }
  .brand-large .mark {
    width: 22px; height: 22px; background: var(--brand-green);
  }
  .brand-large .name {
    font-family: "Montserrat", sans-serif;
    font-weight: 600;
    font-size: 36px;
    letter-spacing: 1px;
    color: var(--silver);
  }

  /* Back */
  .diagonal { position: absolute; inset: 0; }
  .brand-small {
    position: absolute; left: 30px; top: 30px;
    font-family: "Montserrat", sans-serif;
    font-weight: 600;
    font-size: 15px;
    color: var(--card-black);
  }
  .signature {
    position: absolute; right: 34px; top: 22px;
    text-align: right;
    font-family: "Allura", cursive;
    color: var(--brand-green);
    line-height: 1;
  }
  .signature .person { font-size: 46px; display: block; }
  .signature .title { font-size: 34px; display: block; margin-top: 4px; }
  .contact {
    position: absolute; right: 30px; bottom: 28px;
    text-align: right;
    font-family: "Lora", serif;
    font-size: 11.5px;
    line-height: 1.45;
    letter-spacing: .4px;
    color: var(--white);
  }
  .contact .company { color: var(--brand-green); }
</style>
</head>
<body>
  <main class="sheet">
    <section class="card card-front" aria-label="Card front">
      <div class="brand-large">
        <span class="mark"></span>
        <span class="name">Bluestone Advisory</span>
      </div>
    </section>

    <section class="card card-back" aria-label="Card back">
      <svg class="diagonal" width="540" height="309" viewBox="0 0 540 309" aria-hidden="true">
        <polygon points="0,0 255,0 118,309 0,309" fill="var(--brand-green)"/>
      </svg>
      <div class="brand-small">Bluestone Advisory</div>
      <div class="signature">
        <span class="person">Dorian Pelkey</span>
        <span class="title">Principle</span>
      </div>
      <address class="contact" style="font-style:normal">
        <div class="company">Bluestone Advisory &amp; Mgmt, LLC</div>
        <div>Address: 348 West 71st Street, 9th FL New York, NY 10010</div>
        <div>Mobile: 917.806.3971</div>
        <div>Website: bam-hvx.example</div>
      </address>
    </section>
  </main>
</body>
</html>
```